Groovy little Insurance brokerage needs a new look

We have a new logo, but need to work out how to make it work for us!
We are a small insurance broking firm (three staff with different focus and styles), with lots of energy, experience and enthusiasm. A focus on both commercial and domestic market. We would like our cards to show a fresh look - while veering away from the 'run of the mill' insurance industry (often dull) approach.
Updates

Thanks to all for your concepts.

Had some great ideas come back, now just the process of picking which one is going to work best for us...
Will advise when we've had an opportunity to review.

Thanks!
From the team at
Kestrel Dunmore Insurance Brokers

Thanks SO much to all of your for your great designs.  Now just a process of sorting out the favorites.  If yours is eliminated, just want to say a collective thank you for your efforts!

Industry/Entity Type

Business

```html
<!DOCTYPE html>
<html lang="en">
<head>
<meta charset="utf-8">
<title>Kestrel Dunmore Insurance Brokers – Business Card</title>
<link rel="stylesheet" href="https://fonts.googleapis.com/css2?family=Roboto+Slab:wght@400;700&display=swap">
<style>
  :root {
    --teal: #1fb0c6;
    --ink: #333234;
    --paper: #ffffff;
    --mist: #e2e4e6;
    --edge: #4a4a4a;
  }
  * { box-sizing: border-box; margin: 0; padding: 0; }
  html, body {
    width: 1200px;
    height: 669px;
    overflow: hidden;
    background: var(--paper);
  }
  .card {
    position: relative;
    width: 1200px;
    height: 669px;
    border: 2px solid var(--edge);
    overflow: hidden;
    font-family: "Roboto Slab", Georgia, serif;
    color: var(--ink);
    background: radial-gradient(ellipse 80% 70% at 50% 45%, var(--paper) 0%, #f3f4f5 55%, var(--mist) 100%);
  }
  .card__swoosh {
    position: absolute;
    inset: 0;
    width: 100%;
    height: 100%;
  }
  .brand {
    position: absolute;
    left: 315px;
    top: 84px;
    display: flex;
    align-items: center;
    gap: 22px;
  }
  .brand__square {
    width: 143px;
    height: 149px;
    background: var(--teal);
    flex: none;
  }
  .brand__name {
    font-weight: 700;
    font-size: 44px;
    line-height: 1.12;
    color: var(--ink);
  }
  .person {
    position: absolute;
    left: 0;
    right: 0;
    top: 330px;
    text-align: center;
    font-weight: 700;
    font-size: 27px;
    line-height: 34px;
    letter-spacing: 2px;
    color: var(--ink);
  }
  .contact-band {
    position: absolute;
    left: 0;
    right: 0;
    top: 496px;
    height: 40px;
    background: var(--teal);
    color: var(--paper);
    font-size: 25px;
    line-height: 40px;
    letter-spacing: 1.5px;
    text-align: center;
  }
  .contact-band__sep { margin: 0 14px; }
  .address {
    position: absolute;
    left: 0;
    right: 0;
    top: 568px;
    text-align: center;
    font-size: 24px;
    letter-spacing: 1.5px;
    color: var(--ink);
  }
</style>
</head>
<body>
  <div class="card">
    <svg class="card__swoosh" viewBox="0 0 1200 669" aria-hidden="true">
      <path d="M0 500 C 300 360, 700 330, 1200 80 L 1200 150 C 760 390, 360 420, 0 560 Z" fill="#ffffff" opacity="0.85"/>
      <path d="M60 669 C 380 520, 820 470, 1200 250 L 1200 300 C 860 510, 460 560, 150 669 Z" fill="#ffffff" opacity="0.7"/>
    </svg>

    <div class="brand">
      <div class="brand__square"></div>
      <div class="brand__name">Kestrel Dunmore<br>Insurance Brokers</div>
    </div>

    <div class="person">
      <div class="person__name">Orwin</div>
      <div class="person__title">C.E.O</div>
    </div>

    <div class="contact-band">
      T: +00 0000 0000<span class="contact-band__sep">|</span>M:+00 0000 0000<span class="contact-band__sep">|</span>E:abc@abc.com
    </div>

    <div class="address">#123, Street name,City name - 000000</div>
  </div>
</body>
</html>
```